Very Simple/Minimal Business Card Design Project

The company operates in the industrial maritime infrastructure sector in Brazil. You can find more information on our website www.navelquor.com.br WE NEED TO LOOK POWERFUL AND SERIOUS
I have attached a copy of the old cards. We would like something more professional / industrial / sexy that also includes the position.

The card can be double sided or not. We would like you to propose as many options.

Thank you
Updates

Many thanks, do let me know if you have any questions. I am under a lot of time pressure to try and have them printed over the next days or so.

Please could you use the following information

for the address: Rua Tapiraçu, 418 - Centro, Rio de Janeiro, 20135-070, Brasil

for the mobile: +55 21 8372 9041
for the landline: +55 21 4067 3859

and position:  Diretor Geral

Thakn you

Target Market(s)

Shipowners, bankers, industrial companies

Industry/Entity Type

Industrial

Requirements
Must have
• POWERFUL
SERIOUS
SOLID
BIG CORPORATION

```html
<!DOCTYPE html>
<html lang="pt-BR">
<head>
<meta charset="utf-8">
<title>Navelquor Business Card</title>
<link href="https://fonts.googleapis.com/css2?family=Archivo:wght@700;800&family=Open+Sans:wght@400;600&display=swap" rel="stylesheet">
<style>
  :root {
    --page-bg: #e9e9ea;
    --card-bg: #f7f7f7;
    --card-edge: #d6d6d8;
    --brand-blue: #2f3a7e;
    --brand-green: #1f9a4a;
    --brand-green-light: #33b062;
    --band-dark: #2f3130;
    --text-grey: #6b6b6b;
    --text-dark: #3a3a3a;
    --white: #ffffff;
  }
  * { box-sizing: border-box; margin: 0; padding: 0; }
  html, body { width: 1200px; height: 861px; overflow: hidden; }
  body {
    background: var(--page-bg);
    font-family: "Open Sans", Arial, sans-serif;
    position: relative;
  }
  .card {
    position: absolute;
    top: 285px;
    width: 470px;
    height: 290px;
    background: var(--card-bg);
    border-radius: 14px;
    box-shadow: 0 10px 30px rgba(0,0,0,0.18), 0 0 0 1px var(--card-edge);
    overflow: hidden;
  }
  .card--front { left: 90px; }
  .card--back { left: 635px; }
  .card-texture {
    position: absolute; inset: 0;
    background: radial-gradient(circle at 50% 50%, #fbfbfb 0%, #f1f1f1 60%, #e8e8e8 100%);
  }
  .wordmark {
    position: absolute;
    display: flex;
    align-items: center;
    gap: 12px;
    font-family: "Archivo", Arial, sans-serif;
    font-weight: 800;
    color: var(--brand-blue);
    letter-spacing: 0.5px;
    white-space: nowrap;
  }
  .wordmark-square {
    background: var(--brand-green);
    border-radius: 5px;
  }
  .card--front .wordmark { left: 98px; top: 90px; font-size: 38px; }
  .card--front .wordmark-square { width: 62px; height: 62px; }
  .front-url {
    position: absolute; left: 0; right: 0; top: 160px;
    text-align: center;
    font-weight: 600; font-size: 17px;
    color: var(--text-dark);
  }
  .card--back .wordmark { left: 112px; top: 28px; font-size: 30px; }
  .card--back .wordmark-square { width: 54px; height: 54px; }
  .person-name {
    position: absolute; left: 0; right: 0; top: 110px;
    text-align: center;
    font-family: "Archivo", Arial, sans-serif;
    font-weight: 800; font-size: 25px;
    color: var(--brand-blue);
    white-space: nowrap;
  }
  .person-role {
    position: absolute; left: 0; right: 0; top: 141px;
    text-align: center;
    font-family: "Archivo", Arial, sans-serif;
    font-weight: 700; font-size: 15px;
    color: var(--text-grey);
  }
  .address {
    position: absolute; left: 0; right: 0; top: 181px;
    text-align: center;
    font-size: 11.5px; color: var(--text-dark);
    white-space: nowrap;
  }
  .contact-band {
    position: absolute; left: 0; right: 0; top: 200px; height: 54px;
    display: flex;
  }
  .band-green {
    background: linear-gradient(90deg, var(--brand-green), var(--brand-green-light));
    display: flex; flex-direction: column; justify-content: center; gap: 4px;
    align-items: center;
  }
  .band-green--left { width: 100px; align-items: flex-end; padding-right: 6px; }
  .band-green--right { width: 40px; }
  .band-dark {
    flex: 1;
    background: var(--band-dark);
    display: flex; justify-content: space-between; align-items: center;
    padding: 0 10px;
    color: var(--white); font-size: 12px; line-height: 20px;
    white-space: nowrap;
  }
  .band-dark .emails { text-align: right; font-size: 11.5px; }
  .icon { width: 18px; height: 18px; display: block; }
</style>
</head>
<body>

<section class="card card--front" aria-label="Card front">
  <div class="card-texture" role="img" aria-label="Subtle light grey chevron line texture"></div>
  <div class="wordmark"><span class="wordmark-square"></span>NAVELQUOR</div>
  <p class="front-url">www.navelquor.com.br</p>
</section>

<section class="card card--back" aria-label="Card back">
  <div class="card-texture" role="img" aria-label="Subtle light grey chevron line texture"></div>
  <div class="wordmark"><span class="wordmark-square"></span>NAVELQUOR</div>
  <h1 class="person-name">RAFAEL MONTENEGRO</h1>
  <p class="person-role">DIRETOR GERAL</p>
  <p class="address">Rua Tapiraçu, 418 - Centro, Rio de Janeiro, 20135-070, Brasil</p>

  <div class="contact-band">
    <div class="band-green band-green--left">
      <svg class="icon" viewBox="0 0 20 20" aria-label="Phone">
        <circle cx="10" cy="10" r="9" fill="none" stroke="#fff" stroke-width="1.4"/>
        <path d="M6.5 6 l2 0 l0.8 2.2 l-1.2 1 a6 6 0 0 0 2.7 2.7 l1-1.2 l2.2 0.8 l0 2 a1 1 0 0 1 -1 1 a8 8 0 0 1 -7.5 -7.5 a1 1 0 0 1 1 -1z" fill="#fff"/>
      </svg>
      <svg class="icon" viewBox="0 0 20 20" aria-label="Mobile">
        <circle cx="10" cy="10" r="9" fill="none" stroke="#fff" stroke-width="1.4"/>
        <rect x="7" y="5" width="6" height="10" rx="1" fill="#fff"/>
        <rect x="8" y="6.5" width="4" height="6" fill="#1f9a4a"/>
      </svg>
    </div>
    <div class="band-dark">
      <div class="phones">+ 55 21 4067 3859<br>+ 55 21 8372 9041</div>
      <div class="emails">rafael@navelquor.com.br<br>www.navelquor.com.br</div>
    </div>
    <div class="band-green band-green--right">
      <svg class="icon" viewBox="0 0 20 20" aria-label="Email">
        <circle cx="10" cy="10" r="9" fill="none" stroke="#fff" stroke-width="1.4"/>
        <rect x="5.5" y="7" width="9" height="6.5" rx="1" fill="#fff"/>
        <path d="M5.8 7.3 L10 10.5 L14.2 7.3" fill="none" stroke="#1f9a4a" stroke-width="1"/>
      </svg>
      <svg class="icon" viewBox="0 0 20 20" aria-label="Website">
        <circle cx="10" cy="10" r="9" fill="none" stroke="#fff" stroke-width="1.4"/>
        <circle cx="10" cy="10" r="4.5" fill="none" stroke="#fff" stroke-width="1.2"/>
        <path d="M5.5 10 H14.5 M10 5.5 V14.5" stroke="#fff" stroke-width="1"/>
      </svg>
    </div>
  </div>
</section>

</body>
</html>
```